Records Management Company Revamp

We are looking to revamp our web presence, and need a catchy design that helps us to get noticed! We would like the website to be in wordpress. the main requirements are a home page, a landing page template for SEO / PPC, and then a few other pages that can be reused throughout the website.

We are happy to supply content / video etc.

Number of Pages Required

3 page

Font styles to use
Other font styles liked:
• Find fonts listed in attached branding document

Requirements
Must have
• Home page as well as sub pages according to their colours. Need to use colours and fonts set out in branding guide. Attached are examples of home page and sub pages.
Nice to have
• We have uploaded some very basic ideas we have of how we wish the website to look, but looking to have it more professional and fit together. Please see uploaded items.

```html
<!DOCTYPE html>
<html lang="en">
<head>
<meta charset="utf-8">
<title>Vault Keep – Archive Document Storage</title>
<link href="https://fonts.googleapis.com/css2?family=Oswald:wght@400;500;600&family=Open+Sans:wght@400;600;700&display=swap" rel="stylesheet">
<style>
:root{
  --blue:#1b8bc9;
  --blue-dark:#22689c;
  --navy:#1d4f7a;
  --ink:#333;
  --muted:#777;
  --line:#dcdcdc;
  --soft:#f4f4f4;
  --footer:#3a3a3a;
  --white:#fff;
}
*{box-sizing:border-box;margin:0;padding:0}
html,body{width:1200px;height:4444px;overflow:hidden}
body{font-family:"Open Sans",Arial,sans-serif;color:var(--ink);background:var(--white);position:relative}
.abs{position:absolute}
h1,h2,h3,.oswald{font-family:"Oswald","Arial Narrow",sans-serif;font-weight:500}

/* top bar */
.topbar{top:0;left:0;width:1200px;height:53px;border-bottom:1px solid var(--line)}
.social{left:80px;top:12px;display:flex;gap:10px}
.social span{width:30px;height:30px;border-radius:50%;background:var(--blue);display:block}
.top-contact{right:80px;top:15px;display:flex;gap:40px;font-size:16px;color:#555;align-items:center}
.top-contact div{display:flex;gap:10px;align-items:center}

/* nav */
.nav{top:53px;left:0;width:1200px;height:125px}
.logo{left:80px;top:22px;display:flex;align-items:center;gap:10px;font-family:"Oswald",sans-serif;font-size:32px;color:var(--navy);font-weight:600}
.logo i{width:34px;height:34px;background:var(--blue);display:block}
.menu{left:338px;top:48px;display:flex;gap:36px;font-size:15px;color:#888;text-transform:uppercase}
.menu .active{color:var(--blue);font-weight:700;position:relative}
.menu .active:after{content:"";position:absolute;left:50%;top:30px;margin-left:-8px;border:8px solid transparent;border-bottom-color:var(--blue)}

/* hero */
.hero{top:178px;left:0;width:1200px;height:572px;background:linear-gradient(90deg,#e9e4dd 0%,#d8cbb8 45%,#b58c62 100%)}
.hero-people{right:150px;top:10px;width:520px;height:562px;background:linear-gradient(180deg,#c9a67e,#8c6a4a);opacity:.6}
.hero h1{left:80px;top:130px;font-size:52px;line-height:66px;color:#222;text-transform:uppercase;font-weight:600}
.hero p{left:80px;top:275px;width:520px;font-size:19px;line-height:31px;color:#222}
.btn{display:inline-block;background:var(--blue);color:#fff;font-size:15px;font-weight:700;text-transform:uppercase;padding:16px 20px}
.hero .btns{left:80px;top:350px;display:flex;gap:14px}

/* quote form */
.quote{left:80px;top:702px;width:330px;height:519px;background:#fff;border:5px solid var(--blue);box-shadow:0 4px 10px rgba(0,0,0,.15);padding:28px 22px}
.quote h3{font-size:20px;line-height:27px;text-transform:uppercase;color:#222;margin-bottom:22px}
.field{border:1px solid var(--line);height:48px;font-size:13px;color:#666;padding:14px 12px;margin-bottom:10px}
.row{display:flex;gap:10px}.row .field{flex:1}
.field.tall{height:118px}
.quote .btn{display:block;width:150px;margin:16px auto 0;text-align:center;background:var(--blue-dark);padding:14px 0}

/* services */
.services-head{left:444px;top:780px;width:682px}
.services-head h2{font-size:22px;color:var(--blue);text-transform:uppercase}
.services-head p{font-size:14px;line-height:23px;color:#888;width:470px;margin-top:12px}
.view-all{right:74px;top:812px;font-size:15px;font-weight:700;color:#333;display:flex;gap:10px;align-items:center}
.services-line{left:444px;top:885px;width:682px;height:1px;background:var(--line)}
.service{top:912px;width:313px}
.service .ph{height:208px}
.service h4{font-size:22px;color:var(--blue);font-weight:600;margin-top:22px;padding-left:12px;border-left:3px solid var(--blue);line-height:26px}
.service p{font-size:14px;line-height:22px;color:#888;padding-left:15px;margin-top:8px}

/* how it works */
.how-photo{left:0;top:1295px;width:600px;height:631px;background:linear-gradient(135deg,#c8a77a,#8d6b49 60%,#6a5a4a)}
.how{left:600px;top:1295px;width:600px;height:631px;background:linear-gradient(180deg,#3d8fc2,#1f6497)}
.how h2{position:absolute;left:40px;top:60px;font-size:34px;color:#fff;text-transform:uppercase}
.steps{position:absolute;left:40px;top:128px;width:520px}
.step{display:flex;gap:20px;margin-bottom:20px;color:#fff}
.step svg{flex:none}
.step b{display:block;font-size:17px;margin-bottom:4px}
.step span{font-size:13px;line-height:20px;display:block;color:#e6f1f8}

/* benefits */
.benefits{top:1926px;left:0;width:1200px;height:563px;background:var(--soft)}
.benefits h2{left:80px;top:68px;font-size:32px;color:var(--navy);text-transform:uppercase}
.benefits p.lead{left:80px;top:130px;width:600px;font-size:14px;line-height:22px;color:#888}
.tile{width:208px;height:207px;background:#fff;border:1px solid var(--line);display:flex;flex-direction:column;align-items:center;justify-content:center;gap:16px;font-size:18px;font-weight:600;color:var(--blue);text-align:center;line-height:22px}

/* team */
.team h2,.blog h2{width:1200px;text-align:center;font-size:36px;color:var(--navy);text-transform:uppercase}
.member{top:2628px;width:238px;height:410px;background:#fff;border:1px solid var(--line);box-shadow:0 2px 8px rgba(0,0,0,.08);text-align:center}
.member .ph{width:176px;height:176px;border-radius:50%;margin:36px auto 0;background:linear-gradient(180deg,#e3c39a,#b48556);border:4px solid #fff;box-shadow:0 2px 6px rgba(0,0,0,.2)}
.member h4{font-size:22px;color:var(--blue);font-weight:600;margin-top:54px}
.member small{display:block;font-size:13px;color:#777;margin-top:12px}
.member .icons{display:flex;justify-content:center;gap:8px;margin-top:26px}
.member .icons span{width:30px;height:30px;border:1px solid var(--line);display:block}
.member.featured{background:var(--blue);border-color:var(--blue)}
.member.featured h4,.member.featured small{color:#fff}
.member.featured .icons span{border-color:#fff;background:rgba(255,255,255,.2)}

/* testimonial */
.testimonial{top:3096px;left:0;width:1200px;height:430px;background:linear-gradient(180deg,#3b3f42,#1f2326)}
.testimonial .dots{left:567px;top:150px;display:flex;gap:8px}
.testimonial .dots span{width:14px;height:14px;border-radius:50%;border:2px solid #fff}
.testimonial .dots span.on{background:#fff}
.testimonial blockquote{left:210px;top:190px;width:780px;text-align:center;font-style:italic;font-size:18px;line-height:32px;color:#fff}
.testimonial .who{left:0;top:328px;width:1200px;text-align:center;font-style:italic}
.testimonial .who b{color:var(--blue);font-size:17px;display:block}
.testimonial .who span{color:#fff;font-size:13px}

/* blog */
.post{top:3674px;width:334px}
.post .ph{height:213px}
.post .meta{font-size:14px;color:#333;margin-top:18px}
.post h4{font-size:19px;color:var(--blue);font-weight:600;margin-top:12px}
.post p{font-size:14px;line-height:22px;color:#666;margin-top:12px}

/* footer */
.footer{top:4178px;left:0;width:1200px;height:266px;background:var(--footer);color:#fff}
.footer nav{position:absolute;left:80px;top:62px;display:flex;gap:32px;font-size:16px}
.footer nav .active{color:var(--blue)}
.footer .flogo{position:absolute;right:80px;top:52px;display:flex;align-items:center;gap:10px;font-family:"Oswald",sans-serif;font-size:30px;font-weight:600;color:var(--blue)}
.footer .flogo i{width:32px;height:32px;background:var(--blue);display:block}
.footer .rule{position:absolute;left:0;top:142px;width:1200px;height:1px;background:#555}
.fc{position:absolute;top:175px;display:flex;gap:16px;align-items:center;font-size:13px;line-height:20px}
.fc .ic{width:46px;height:46px;border-radius:50%;background:#fff;display:flex;align-items:center;justify-content:center;flex:none}
</style>
</head>
<body>

<header>
  <div class="abs topbar">
    <div class="abs social"><span></span><span></span><span></span><span></span></div>
    <div class="abs top-contact">
      <div><svg width="22" height="16" viewBox="0 0 22 16"><rect x="1" y="1" width="20" height="14" fill="none" stroke="#555" stroke-width="2"/><path d="M1 1l10 8 10-8" fill="none" stroke="#555" stroke-width="2"/></svg>hello@vaultkeep.example</div>
      <div><svg width="20" height="20" viewBox="0 0 24 24"><path d="M6 2l4 5-2 3c1 3 3 5 6 6l3-2 5 4-3 4C10 21 3 14 2 5z" fill="#555"/></svg>123-456-7890</div>
    </div>
  </div>
  <div class="abs nav">
    <div class="abs logo"><i></i>VAULT KEEP</div>
    <nav class="abs menu">
      <span class="active">Home</span><span>What we offer</span><span>How it works</span><span>Services</span><span>Team</span><span>Testimonial</span><span>Contact</span>
      <svg width="22" height="22" viewBox="0 0 24 24"><circle cx="10" cy="10" r="7" fill="none" stroke="#1b8bc9" stroke-width="3"/><path d="M15 15l7 7" stroke="#1b8bc9" stroke-width="3"/></svg>
    </nav>
  </div>
</header>

<section class="abs hero">
  <div class="abs hero-people" role="img" aria-label="Businessman with clipboard beside stacked archive boxes"></div>
  <h1 class="abs">Archive Document Storage &amp;<br>Records Management</h1>
  <p class="abs">Professional, secure and reliable. Vault Keep is your new home for all your archiving needs.</p>
  <div class="abs btns"><span class="btn">Learn more</span><span class="btn">Contact us</span></div>
</section>

<form class="abs quote">
  <h3>Find out how cost effective we are in storing your archive boxes.</h3>
  <div class="row"><div class="field">Name :</div><div class="field">Phone :</div></div>
  <div class="field">Email :</div>
  <div class="field">Approx. Number of Boxes :</div>
  <div class="field tall">Message / Comments :</div>
  <span class="btn">Submit now</span>
</form>

<section>
  <div class="abs services-head">
    <h2>We service the Melbourne area</h2>
    <p>Lorem ipsum dolor sit amet, consectetur adipiscing elit, sed do eiusmod tempor incididunt ut labore et dolore magna aliqua.</p>
  </div>
  <div class="abs view-all">VIEW ALL SERVICES <svg width="24" height="24" viewBox="0 0 24 24"><circle cx="12" cy="12" r="10" fill="none" stroke="#1b8bc9" stroke-width="2"/><path d="M8 12h8M13 8l4 4-4 4" fill="none" stroke="#1b8bc9" stroke-width="2"/></svg></div>
  <div class="abs services-line"></div>
  <div class="abs service" style="left:444px">
    <div class="ph" role="img" aria-label="Warehouse shelves of archive boxes" style="background:linear-gradient(135deg,#e2c07e,#a87f45)"></div>
    <h4>Offsite Storage</h4>
    <p>Store all your archives in our secure offsite warehouse</p>
  </div>
  <div class="abs service" style="left:788px">
    <div class="ph" role="img" aria-label="Pile of shredded paper" style="background:linear-gradient(135deg,#e8eef4,#9fb3c6)"></div>
    <h4>Document Shredding</h4>
    <p>Lorem ipsum dolor sit amet, consectetur adipiscing elit.</p>
  </div>
</section>

<section>
  <div class="abs how-photo" role="img" aria-label="Staff packing and labelling archive boxes in a warehouse"></div>
  <div class="abs how">
    <h2>How Vault Keep works</h2>
    <div class="steps">
      <div class="step"><svg width="46" height="46" viewBox="0 0 46 46"><path d="M6 14l17-8 17 8v20l-17 8-17-8z M6 14l17 8 17-8 M23 22v20" fill="none" stroke="#fff" stroke-width="3"/></svg><div><b>We deliver boxes and labels</b><span>If you need them, we get you started with all the essentials to prepare your archives.</span></div></div>
      <div class="step"><svg width="46" height="46" viewBox="0 0 46 46"><rect x="10" y="4" width="26" height="36" fill="none" stroke="#fff" stroke-width="3"/><path d="M15 14h16M15 21h16M15 28h10" stroke="#fff" stroke-width="3"/></svg><div><b>We pick up your documents</b><span>When your boxes are ready, let us know and we'll come by and collect your documents.</span></div></div>
      <div class="step"><svg width="46" height="46" viewBox="0 0 46 46"><rect x="6" y="8" width="34" height="30" fill="none" stroke="#fff" stroke-width="3"/><path d="M6 18h34M6 28h34" stroke="#fff" stroke-width="3"/></svg><div><b>We Store Your Documents</b><span>Your documents are stored in our secure purpose-built facility in Moorabbin/Braeside.</span></div></div>
      <div class="step"><svg width="46" height="46" viewBox="0 0 46 46"><path d="M6 10h34v26H6z M6 10l17 14 17-14" fill="none" stroke="#fff" stroke-width="3"/></svg><div><b>We Retrieve &amp; Deliver Your Documents</b><span>When you need your documents, just call or email us and we'll get them to you!</span></div></div>
      <div class="step"><svg width="46" height="46" viewBox="0 0 46 46"><rect x="8" y="6" width="30" height="16" fill="none" stroke="#fff" stroke-width="3"/><path d="M12 26v14M18 26v14M24 26v14M30 26v14M36 26v14" stroke="#fff" stroke-width="3"/></svg><div><b>We Can Securely Destroy</b><span>We can work with you on determining which documents can be securely destroyed and do this for you!</span></div></div>
    </div>
  </div>
</section>

<section class="abs benefits">
  <h2 class="abs">Vault Keep Benefits</h2>
  <p class="abs lead">Lorem ipsum dolor sit amet, consectetur adipiscing elit, sed do eiusmod tempor incididunt ut labore et dolore magna aliqua. Ut enim ad minim veniam, quis nostrud exercitation ullamco laboris nisi ut aliquip ex ea commodo consequat. Duis aute irure dolor in reprehenderit in voluptate velit esse cillum dolore eu fugiat nulla pariatur.</p>
  <div class="abs tile" style="left:702px;top:65px"><svg width="60" height="56" viewBox="0 0 60 56"><path d="M8 18l22-10 22 10v26L30 54 8 44z M8 18l22 10 22-10 M30 28v26 M8 18L2 8l22-6 6 6" fill="none" stroke="#444" stroke-width="3"/></svg>Heading</div>
  <div class="abs tile" style="left:909px;top:65px"><svg width="46" height="56" viewBox="0 0 46 56"><rect x="4" y="4" width="38" height="48" fill="none" stroke="#444" stroke-width="3"/><rect x="14" y="24" width="18" height="16" fill="#444"/><path d="M17 24v-5a6 6 0 0 1 12 0v5" fill="none" stroke="#444" stroke-width="3"/></svg>No lock-in<br>contracts</div>
  <div class="abs tile" style="left:80px;top:272px"><svg width="60" height="56" viewBox="0 0 60 56"><circle cx="22" cy="16" r="9" fill="#444"/><path d="M6 46c0-12 8-18 16-18s16 6 16 18z" fill="#444"/><circle cx="42" cy="30" r="9" fill="none" stroke="#444" stroke-width="3"/><path d="M48 36l8 8" stroke="#444" stroke-width="4"/></svg>Expert Staff</div>
  <div class="abs tile" style="left:287px;top:272px"><svg width="70" height="50" viewBox="0 0 70 50"><path d="M16 8h30v26H16z M46 16h12l8 10v8H46" fill="none" stroke="#444" stroke-width="3"/><circle cx="24" cy="40" r="6" fill="#444"/><circle cx="54" cy="40" r="6" fill="#444"/><path d="M2 14h10M4 22h8M6 30h6" stroke="#444" stroke-width="3"/></svg>Speedy Retrievals</div>
  <div class="abs tile" style="left:494px;top:272px"><svg width="64" height="56" viewBox="0 0 64 56"><rect x="4" y="6" width="56" height="34" fill="none" stroke="#444" stroke-width="3"/><path d="M24 50h16M32 40v10" stroke="#444" stroke-width="3"/><circle cx="32" cy="23" r="10" fill="none" stroke="#444" stroke-width="2"/><path d="M22 23h20M32 13v20" stroke="#444" stroke-width="2"/></svg>Simple Online<br>Software</div>
  <div class="abs tile" style="left:701px;top:272px"><svg width="60" height="56" viewBox="0 0 60 56"><circle cx="24" cy="24" r="20" fill="none" stroke="#444" stroke-width="3"/><path d="M30 16h-9a4 4 0 0 0 0 8h6a4 4 0 0 1 0 8h-9M24 10v28" fill="none" stroke="#444" stroke-width="3"/><path d="M40 40h14v14H40z" fill="#444"/></svg>Competitive Pricing</div>
  <div class="abs tile" style="left:908px;top:272px"><svg width="56" height="60" viewBox="0 0 56 60"><path d="M28 2l24 10v18c0 16-12 26-24 28C16 56 4 46 4 30V12z" fill="none" stroke="#444" stroke-width="3"/><rect x="6" y="24" width="44" height="12" fill="#444"/></svg>Money Back<br>Guarantee</div>
</section>

<section class="team">
  <h2 class="abs" style="top:2548px;left:0">Our Team</h2>
  <div class="abs member" style="left:80px"><div class="ph" role="img" aria-label="Portrait of a staff member holding a box"></div><h4>Owen Harte</h4><small>Storage Manager</small><div class="icons"><span></span><span></span><span></span><span></span></div></div>
  <div class="abs member featured" style="left:352px"><div class="ph" role="img" aria-label="Portrait of a delivery staff member with a box"></div><h4>Liam Corder</h4><small>Stock Deliver</small><div class="icons"><span></span><span></span><span></span><span></span></div></div>
  <div class="abs member" style="left:614px"><div class="ph" role="img" aria-label="Portrait of a staff member with a cap"></div><h4>Tara Wells</h4><small>Storage Manager</small><div class="icons"><span></span><span></span><span></span><span></span></div></div>
  <div class="abs member" style="left:883px"><div class="ph" role="img" aria-label="Portrait of a delivery driver by a van"></div><h4>Niko Brandt</h4><small>Stock Deliver</small><div class="icons"><span></span><span></span><span></span><span></span></div></div>
</section>

<section class="abs testimonial" role="img" aria-label="Dark warehouse aisle background">
  <svg class="abs" style="left:578px;top:64px" width="44" height="40" viewBox="0 0 44 40"><path d="M2 22c0-12 6-18 16-20v6c-5 2-7 5-7 9h7v18H2z M24 22c0-12 6-18 16-20v6c-5 2-7 5-7 9h7v18H24z" fill="#1b8bc9"/></svg>
  <div class="abs dots"><span></span><span class="on"></span><span></span></div>
  <svg class="abs" style="left:170px;top:230px" width="20" height="40" viewBox="0 0 20 40"><path d="M18 2L2 20l16 18" fill="none" stroke="#fff" stroke-width="2"/></svg>
  <svg class="abs" style="left:1010px;top:230px" width="20" height="40" viewBox="0 0 20 40"><path d="M2 2l16 18L2 38" fill="none" stroke="#fff" stroke-width="2"/></svg>
  <blockquote class="abs">Lorem Ipsum is simply dummy text of the printing and typesetting industry. Lorem Ipsum has been the industry's standard dummy text ever since the 1500s, when an unknown printer took a galley of type and scrambled it to make a type specimen book.</blockquote>
  <div class="abs who"><b>- Mara Quill</b><span>Student</span></div>
</section>

<section class="blog">
  <h2 class="abs" style="top:3590px;left:0">Recent Blog Update</h2>
  <article class="abs post" style="left:80px"><div class="ph" role="img" aria-label="Warehouse staff carrying boxes" style="background:linear-gradient(135deg,#8fa6bd,#c49a6a)"></div><div class="meta"><b><i>16 January</i></b> <i>By Author</i></div><h4>Excepteur sint occaecat cupidatat</h4><p>Lorem Ipsum is simply dummy text of the printing and sed do eiusmod typesetting industry.</p></article>
  <article class="abs post" style="left:433px"><div class="ph" role="img" aria-label="Stacks of cardboard boxes with a hand trolley" style="background:linear-gradient(135deg,#d8c3a0,#9c7a50)"></div><div class="meta"><b><i>16 January</i></b> <i>By Author</i></div><h4>Excepteur sint occaecat cupidatat</h4><p>Lorem Ipsum is simply dummy text of the printing and sed do eiusmod typesetting industry.</p></article>
  <article class="abs post" style="left:788px"><div class="ph" role="img" aria-label="Workers in hard hats checking stock" style="background:linear-gradient(135deg,#e3e3e3,#c8945a)"></div><div class="meta"><b><i>16 January</i></b> <i>By Author</i></div><h4>Excepteur sint occaecat cupidatat</h4><p>Lorem Ipsum is simply dummy text of the printing and sed do eiusmod typesetting industry.</p></article>
  <span class="abs btn" style="left:526px;top:4068px;background:var(--blue-dark);padding:14px 22px">Go to blog</span>
</section>

<footer class="abs footer">
  <nav><span class="active">Home</span><span>What we offer</span><span>How it works</span><span>Services</span><span>Team</span><span>Testimonial</span><span>Contact</span></nav>
  <div class="flogo"><i></i>VAULT KEEP</div>
  <div class="rule"></div>
  <div class="fc" style="left:80px"><div class="ic"><svg width="18" height="22" viewBox="0 0 18 24"><path d="M9 1a8 8 0 0 1 8 8c0 6-8 14-8 14S1 15 1 9a8 8 0 0 1 8-8z" fill="#3a3a3a"/><circle cx="9" cy="9" r="3" fill="#fff"/></svg></div><div>123, Address, State Name,<br>Street Name, City, Zip Code</div></div>
  <div class="fc" style="left:345px"><div class="ic"><svg width="20" height="20" viewBox="0 0 24 24"><path d="M6 2l4 5-2 3c1 3 3 5 6 6l3-2 5 4-3 4C10 21 3 14 2 5z" fill="#3a3a3a"/></svg></div><div>123-456-789</div></div>
  <div class="fc" style="left:617px"><div class="ic"><svg width="22" height="16" viewBox="0 0 22 16"><rect x="1" y="1" width="20" height="14" fill="none" stroke="#3a3a3a" stroke-width="2"/><path d="M1 1l10 8 10-8" fill="none" stroke="#3a3a3a" stroke-width="2"/></svg></div><div>hello@vaultkeep.example</div></div>
  <div class="fc" style="left:894px"><div class="ic"><svg width="22" height="22" viewBox="0 0 24 24"><circle cx="12" cy="12" r="10" fill="none" stroke="#3a3a3a" stroke-width="2"/><path d="M15 9a4 4 0 1 0 0 6" fill="none" stroke="#3a3a3a" stroke-width="2"/></svg></div><div>© VAULT KEEP - 2018<br>All Rights Reserved.</div></div>
</footer>

</body>
</html>
```